Infographic - Iceberg Strategy Process

We need to develop a simple infographic that shows our process for running a team corporate strategy day. the aim is to simply outline the steps and show that most of the work happens well before a team meets for the company's 'off-site' or strategy day (the work that happens below the waterline). See our website for style reference harlowtqe.com

We are team strategy facilitators. We facilitate corporate team strategy days that usually run for 1 or 2 days.

We call our process a collaborative strategy process, because we seeking input and contribution from our clients staff, customers and clients in the weeks ahead of the actual facilitated strategy day.

We believe this is the best way to develop a winning strategy is to talk, engage and generate insight from the people you deliver value to.

Most companies (and teams) think that running a successful team strategy day (or workshop) is about getting their team into a room for the workshop and brainstorming ideas.
It's not. In fact the workshop happens toward the process and there are some key steps that need to happen well before the team ever gets into the room - this is what we are trying to portray in the infographic.

We describe the process as being like an iceberg - meaning that the team strategy day (workshop) is really only the the 'tip of the iceberg' and most of the work is done by talking to leaders, staff and clients well before the teams gets together in a room for the strategy day workshop. The pre-workshop steps are often or never undertaken.

We describe the steps before the workshop as being like that part of an iceberg that's 'below the water' because they're the necessary steps that the workshop attendees never see but they makes up the majority of the work (Only 1/10th of an iceberg is above the water http://en.frostlexica.org/wiki/Iceberg - See and read the overview section)

Corwin

https://slides.penvarrow.net/deck/d/7kTmwuzofaeQ3-X8LpbR2nGdCvhYsNeWq5jx0LaBoc4/pub?start=false&loop=false&delayms=60000

Target Market(s)

Businesses and corporate teams in business, finance and professional services

Industry/Entity Type

Call

Font styles to use
Sans Serif

Requirements
Must have
• Harlow TQE Logo
• Harlow TQE website reference
• clean, clear design, alignment with Logo colours (logo .png attached)
• Alignment with design of our website style - clean and corporate. We use Google fonts like Raleway (for headings), Merriweather (for content) in our documents

```html
<!DOCTYPE html>
<html lang="en">
<head>
<meta charset="utf-8">
<title>Collaborative Strategy – The Iceberg Process | Harlow TQE</title>
<link rel="stylesheet" href="https://fonts.googleapis.com/css2?family=Montserrat:wght@700;800&family=Roboto:wght@400;700&display=swap">
<style>
  :root {
    --bg: #efefef;
    --ink: #262626;
    --ice: #4fd6f5;
    --sky: #3ba6d0;
    --blue: #2a6fba;
    --navy: #1b3a5a;
    --orange: #f26b21;
    --red: #c91024;
    --line: #333333;
    --white: #ffffff;
  }
  * { margin: 0; padding: 0; box-sizing: border-box; }
  html, body { width: 1200px; height: 2581px; overflow: hidden; background: var(--bg); }
  .canvas { position: relative; width: 1200px; height: 2581px; font-family: "Roboto", Arial, sans-serif; color: var(--ink); }
  .artwork { position: absolute; left: 0; top: 0; }

  .brand { position: absolute; left: 226px; top: 39px; width: 753px; height: 133px; background: #f8f8f8;
           display: flex; align-items: center; justify-content: center; }
  .brand-name { font-family: "Montserrat", Arial, sans-serif; font-weight: 800; font-size: 104px; letter-spacing: -2px; color: var(--ink); line-height: 1; }

  .title { position: absolute; left: 124px; top: 316px; font-family: "Montserrat", Arial, sans-serif; font-weight: 800;
           font-size: 42px; line-height: 50px; color: var(--ink); text-transform: uppercase; }

  .step-card { position: absolute; left: 82px; width: 718px; color: var(--white); padding: 10px 16px;
               font-size: 19.5px; line-height: 23px; box-shadow: 5px 5px 0 rgba(0,0,0,.18); }
  .step-card h3 { font-size: 20px; font-weight: 700; line-height: 23px; }
  .step-card p { margin: 0; }
  .step-card .gap { height: 23px; }
  .step-card .indent { padding-left: 200px; }
  .card-feedback { top: 1331px; height: 144px; background: var(--ice); }
  .card-map { top: 1514px; height: 140px; background: var(--sky); }
  .card-workshop { top: 1697px; height: 172px; background: var(--blue); }
  .card-insight { top: 1924px; height: 206px; background: var(--navy); }
  .card-scan { top: 2180px; height: 150px; background: var(--orange); }
  .card-purpose { top: 2364px; height: 142px; background: var(--red); }

  .band-label { font-family: "Roboto", Arial, sans-serif; font-weight: 700; font-size: 23px; fill: var(--white); }
  .time-label { font-family: "Roboto", Arial, sans-serif; font-weight: 700; font-size: 22px; fill: var(--ink); }
</style>
</head>
<body>
<div class="canvas">
  <svg class="artwork" width="1200" height="2581" viewBox="0 0 1200 2581" aria-hidden="true">
    <line x1="45" y1="226" x2="1160" y2="226" stroke="var(--ice)" stroke-width="4" stroke-dasharray="0 11" stroke-linecap="round"/>

    <g fill="none" stroke="var(--line)" stroke-width="4">
      <polyline points="80,338 80,538 301,538 301,1269 835,1269 835,2480"/>
    </g>
    <g fill="var(--bg)" stroke="var(--line)" stroke-width="4">
      <circle cx="80" cy="338" r="7"/>
      <circle cx="301" cy="538" r="7"/>
      <circle cx="301" cy="1269" r="7"/>
      <circle cx="835" cy="1269" r="7"/>
    </g>

    <polygon points="645,308 770,678 520,678" fill="var(--ice)"/>
    <polygon points="516,688 774,688 805,783 485,783" fill="var(--sky)"/>
    <polygon points="481,796 809,796 842,895 448,895" fill="var(--blue)"/>
    <polygon points="443,910 847,910 880,1007 410,1007" fill="var(--navy)"/>
    <polygon points="405,1022 885,1022 918,1121 372,1121" fill="var(--orange)"/>
    <polygon points="367,1136 923,1136 961,1248 329,1248" fill="var(--red)"/>

    <text class="band-label" text-anchor="middle"><tspan x="645" y="610">Communicate</tspan><tspan x="645" y="638">&amp; Feedback</tspan></text>
    <text class="band-label" x="645" y="744" text-anchor="middle">Strategy Map</text>
    <text class="band-label" x="645" y="854" text-anchor="middle">Team Strategy Day</text>
    <text class="band-label" x="645" y="967" text-anchor="middle">Customer and Staff Insight</text>
    <text class="band-label" x="645" y="1080" text-anchor="middle">Secondary (Desk) Research</text>
    <text class="band-label" x="645" y="1199" text-anchor="middle">Kickoff and Scoping</text>

    <g stroke="var(--line)" stroke-width="4" stroke-dasharray="0 11" stroke-linecap="round">
      <line x1="70" y1="683" x2="285" y2="683"/>
      <line x1="70" y1="792" x2="285" y2="792"/>
      <line x1="70" y1="903" x2="285" y2="903"/>
      <line x1="70" y1="1015" x2="285" y2="1015"/>
      <line x1="70" y1="1129" x2="285" y2="1129"/>
    </g>
    <text class="time-label" text-anchor="middle"><tspan x="183" y="612">2 Weeks after</tspan><tspan x="183" y="640">Workshop</tspan></text>
    <text class="time-label" text-anchor="middle"><tspan x="183" y="726">1 Week after</tspan><tspan x="183" y="754">Workshop</tspan></text>
    <text class="time-label" x="183" y="853" text-anchor="middle">Workshop Week</text>
    <text class="time-label" x="183" y="966" text-anchor="middle">1 Week to go</text>
    <text class="time-label" x="183" y="1079" text-anchor="middle">2 Weeks to go</text>
    <text class="time-label" x="183" y="1198" text-anchor="middle">3 Weeks to go</text>
    <polygon points="309,616 327,626 309,636" fill="var(--ice)"/>
    <polygon points="309,727 327,737 309,747" fill="var(--sky)"/>
    <polygon points="309,835 327,845 309,855" fill="var(--blue)"/>
    <polygon points="309,948 327,958 309,968" fill="var(--navy)"/>
    <polygon points="309,1061 327,1071 309,1081" fill="var(--orange)"/>
    <polygon points="309,1180 327,1190 309,1200" fill="var(--red)"/>

    <g fill="none" stroke-width="3" stroke-dasharray="8 6">
      <polyline points="776,626 1110,626 1110,1400 882,1400" stroke="var(--ice)"/>
      <polyline points="811,737 1090,737 1090,1583 882,1583" stroke="var(--sky)"/>
      <polyline points="848,845 1070,845 1070,1785 882,1785" stroke="var(--blue)"/>
      <polyline points="886,958 1050,958 1050,2028 882,2028" stroke="var(--navy)"/>
      <polyline points="924,1071 1030,1071 1030,2254 882,2254" stroke="var(--orange)"/>
      <polyline points="964,1190 1010,1190 1010,2441 882,2441" stroke="var(--red)"/>
    </g>
    <g>
      <circle cx="770" cy="626" r="6" fill="var(--ice)"/>
      <circle cx="805" cy="737" r="6" fill="var(--sky)"/>
      <circle cx="842" cy="845" r="6" fill="var(--blue)"/>
      <circle cx="880" cy="958" r="6" fill="var(--navy)"/>
      <circle cx="918" cy="1071" r="6" fill="var(--orange)"/>
      <circle cx="958" cy="1190" r="6" fill="var(--red)"/>
    </g>
    <polygon points="884,1389 862,1400 884,1411" fill="var(--ice)"/>
    <polygon points="884,1572 862,1583 884,1594" fill="var(--sky)"/>
    <polygon points="884,1774 862,1785 884,1796" fill="var(--blue)"/>
    <polygon points="884,2017 862,2028 884,2039" fill="var(--navy)"/>
    <polygon points="884,2243 862,2254 884,2265" fill="var(--orange)"/>
    <polygon points="884,2430 862,2441 884,2452" fill="var(--red)"/>

    <g stroke="var(--line)" stroke-width="3">
      <circle cx="835" cy="1400" r="8" fill="var(--ice)"/>
      <circle cx="835" cy="1583" r="8" fill="var(--sky)"/>
      <circle cx="835" cy="1785" r="8" fill="var(--blue)"/>
      <circle cx="835" cy="2028" r="8" fill="var(--navy)"/>
      <circle cx="835" cy="2254" r="8" fill="var(--orange)"/>
      <circle cx="835" cy="2441" r="8" fill="var(--red)"/>
    </g>
  </svg>

  <header class="brand"><span class="brand-name">HARLOWTQE</span></header>

  <h1 class="title">Collaborative<br>Strategy<br>The Iceberg<br>Process</h1>

  <section class="step-card card-feedback">
    <h3>Seek Feedback &amp; Communication</h3>
    <p>Communicate to the workshop group &amp; seek feedback.</p>
    <p>Incorporate feedback into strategy document and tweak where needed.</p>
    <p>Coach the team to be your “market strategy evangelists” to communicate the strategy throughout the organisation.</p>
  </section>

  <section class="step-card card-map">
    <h3>Create Strategy Map &amp; Strategy Summary</h3>
    <p>Create a strategy map on one page</p>
    <p>Create a Strategy Summary Deck in SlideForge (10-12 slides)</p>
    <p>Create an action plan and responsibility pages for pricing, services, target market and promotio strategies</p>
  </section>

  <section class="step-card card-workshop">
    <h3>Team Strategy Workshop</h3>
    <p>Define or review the purpose - “the reason your company exists”</p>
    <p>1. Blue Sky - Create/Define your ideal future</p>
    <p>2. Objectives &amp; Goals - Define your goals &amp; objectives</p>
    <p>3. Positioning - Define market positionin vs competitors and alternatives</p>
    <p>4. Critical Issues - Define critical issues for success</p>
    <p>5. Roadmap - Create a 12 month roadmap to meet objectives</p>
  </section>

  <section class="step-card card-insight">
    <h3>Generate Insight</h3>
    <p>Generate insight on your company, customer and competitors via:</p>
    <p>1/ Customer surveys &amp; conversations</p>
    <p>2. Staff surveys &amp; conversations</p>
    <p>3. Workshop attendee interviews</p>
    <div class="gap"></div>
    <p>Ask for ideas on “How do you win?”, “What should you be doin?” and</p>
    <p>“If you were running things, what would you do?”</p>
  </section>

  <section class="step-card card-scan">
    <h3>Scan the Environment and Hypothesis</h3>
    <p>Internal Scan - Review past strategy documents, marketing plans, website</p>
    <p>External Scan - Assess competitors and alternatives.</p>
    <p class="indent">Look at the impact technology has on decision making</p>
    <p>Develop Hypothesis - develop your marketing strategy hypothesis for testing</p>
  </section>

  <section class="step-card card-purpose">
    <h3>Define the Purpose of the Workshop</h3>
    <p>Meet with leaders, senior management and key stakeholders.</p>
    <p>Define what a successful strategy day will look like.</p>
    <p>Look for clashes and common ground and create a brief.</p>
    <p>Finally, make a list of workshop participants.</p>
  </section>
</div>
</body>
</html>
```